Wedding Ceremony Equipment Hire Business Card

I need a business card design for a new business I created called Altar Outfitters. We hire out Wedding Ceremony equipment and decorations mainly for beach and garden wedding ceremonies that include delivery, set up and dismantle. We do offer DIY Chair Hire as well.
I'd like to have a similar design and colours to our website:
www.altaroutfitters.com.au
If possible would like the front to incorporate our information and logo and the back to have two faded example pictures of our wedding ceremonies.
I have attached two photos and our logo. Please let me know if you need a better pic of our logo though.

Target Market(s)

Newly engaged couples, aged 25 and upwards

Industry/Entity Type

Wedding

Contact Information for Business Card

Altar Outfitters
Mira Tolson
0412 871 964
altaroutfitters@mailbox-example.com
www.socialpage-example.com/AltarOutfitters

```html
<!DOCTYPE html>
<html lang="en">
<head>
<meta charset="utf-8">
<title>Altar Outfitters – Business Card Concepts</title>
<link rel="stylesheet" href="https://fonts.googleapis.com/css2?family=Open+Sans:wght@400;600;700&display=swap">
<style>
  :root{
    --backdrop:#eceeed;
    --mint:#9fc5b9;
    --mint-soft:#c4ddd5;
    --mint-pale:#e3efeb;
    --charcoal:#2b2926;
    --ink:#222222;
    --white:#ffffff;
    --sky:#5d93d8;
    --grass:#6f8a3e;
    --sea:#2f63b8;
    --sand:#d2a877;
  }
  *{box-sizing:border-box;margin:0;padding:0}
  html,body{width:1200px;height:772px;overflow:hidden}
  body{background:var(--backdrop);font-family:"Open Sans",Arial,sans-serif;color:var(--ink);position:relative}

  .option-number{position:absolute;font-size:26px;font-weight:400;color:var(--ink);line-height:1}
  .option-number.one{left:282px;top:24px}
  .option-number.two{left:889px;top:18px}

  .card{position:absolute;overflow:hidden;background:var(--white);box-shadow:0 12px 10px -8px rgba(0,0,0,.28)}
  .card-one-front{left:38px;top:60px;width:532px;height:316px;
    background:linear-gradient(100deg,var(--mint) 0%,var(--white) 45%,var(--mint-soft) 70%,var(--mint) 100%)}
  .card-two-front{left:631px;top:62px;width:530px;height:315px}
  .card-one-back{left:38px;top:415px;width:532px;height:317px;
    background:linear-gradient(200deg,var(--white) 0%,var(--mint-pale) 40%,var(--mint) 100%)}
  .card-two-back{left:625px;top:415px;width:531px;height:315px}

  .side-band{position:absolute;top:0;bottom:0;background:var(--charcoal)}
  .card-one-front .side-band{right:0;width:35px}
  .card-one-back .side-band{left:0;width:37px}

  .top-band{position:absolute;left:0;right:0;top:0;background:var(--mint)}
  .card-two-front .top-band{height:130px}
  .card-two-back .top-band{height:130px}

  .flourish{position:absolute;border-radius:50%;opacity:.45;
    background:radial-gradient(ellipse at center,var(--mint-pale) 0%,rgba(227,239,235,0) 70%)}

  .brand-name{position:absolute;font-weight:600;color:var(--charcoal);white-space:nowrap;letter-spacing:.5px}
  .card-one-front .brand-name{left:36px;top:28px;font-size:30px}
  .card-two-front .brand-name{left:0;right:0;top:40px;text-align:center;font-size:32px}
  .card-one-back .brand-name{left:318px;top:62px;font-size:22px}

  .holder-name{position:absolute;font-weight:700;font-size:17px;color:var(--ink)}
  .card-one-front .holder-name{left:162px;top:134px}
  .card-two-front .holder-name{left:208px;top:145px}

  .contact-list{position:absolute;list-style:none}
  .card-one-front .contact-list{left:42px;top:170px}
  .card-two-front .contact-list{left:88px;top:183px}
  .contact-list li{display:flex;align-items:center;height:29.5px;font-size:17px;white-space:nowrap}
  .contact-list svg{width:16px;height:16px;margin-right:10px;flex:none}

  .ceremony-photo{position:absolute}
  .photo-garden{background:linear-gradient(180deg,var(--sky) 0%,#9ab7d6 35%,var(--grass) 55%,#4f6a2a 100%)}
  .photo-beach{background:linear-gradient(180deg,var(--sea) 0%,#5f8fd4 35%,#e6e2da 55%,var(--sand) 75%,#c0915c 100%)}
  .card-one-back .photo-garden{left:56px;top:13px;width:248px;height:175px}
  .card-one-back .photo-beach{left:263px;top:153px;width:256px;height:150px}
  .card-two-back .photo-garden{left:26px;top:25px;width:247px;height:175px}
  .card-two-back .photo-beach{left:256px;top:130px;width:256px;height:165px}
</style>
</head>
<body>
  <div class="option-number one">1</div>
  <div class="option-number two">2</div>

  <svg width="0" height="0" style="position:absolute">
    <defs>
      <symbol id="icon-phone" viewBox="0 0 16 16"><path d="M4 1.5 6 4.5 4.8 6c.8 1.9 2.3 3.5 4.2 4.3L10.4 9l3 2-1 2.8C7.2 13.6 2.4 8.8 2.2 3.6Z" fill="none" stroke="#222" stroke-width="1.3" stroke-linejoin="round"/></symbol>
      <symbol id="icon-mail" viewBox="0 0 16 16"><rect x="1.5" y="3.5" width="13" height="9" fill="none" stroke="#222" stroke-width="1.2"/><path d="M1.5 3.5 8 9l6.5-5.5" fill="none" stroke="#222" stroke-width="1.2"/></symbol>
      <symbol id="icon-globe" viewBox="0 0 16 16"><circle cx="8" cy="8" r="6.5" fill="none" stroke="#222" stroke-width="1.1"/><ellipse cx="8" cy="8" rx="3" ry="6.5" fill="none" stroke="#222" stroke-width="1"/><path d="M1.5 8h13M2.5 5h11M2.5 11h11" stroke="#222" stroke-width="1"/></symbol>
      <symbol id="icon-square" viewBox="0 0 16 16"><rect x="2" y="2" width="12" height="12" fill="none" stroke="#222" stroke-width="1.3"/></symbol>
    </defs>
  </svg>

  <!-- Option 1, front -->
  <section class="card card-one-front">
    <div class="flourish" role="img" aria-label="Pale mint swirl ornament" style="left:300px;top:-10px;width:230px;height:330px"></div>
    <div class="flourish" role="img" aria-label="Pale mint swirl ornament" style="left:-40px;top:120px;width:220px;height:200px"></div>
    <div class="side-band"></div>
    <div class="brand-name">Altar Outfitters</div>
    <div class="holder-name">Mira Tolson</div>
    <ul class="contact-list">
      <li><svg><use href="#icon-phone"/></svg>0412 871 964</li>
      <li><svg><use href="#icon-mail"/></svg>altaroutfitters@mailbox-example.com</li>
      <li><svg><use href="#icon-globe"/></svg>www.altaroutfitters.com.au</li>
      <li><svg><use href="#icon-square"/></svg>www.socialpage-example.com/AltarOutfitters</li>
    </ul>
  </section>

  <!-- Option 2, front -->
  <section class="card card-two-front">
    <div class="top-band"></div>
    <div class="flourish" role="img" aria-label="Light mint swirl ornament" style="left:0;top:0;width:160px;height:130px"></div>
    <div class="flourish" role="img" aria-label="Light mint swirl ornament" style="right:0;top:0;width:170px;height:130px"></div>
    <div class="flourish" role="img" aria-label="Faint mint swirl ornament" style="left:-10px;top:180px;width:150px;height:140px"></div>
    <div class="brand-name">Altar Outfitters</div>
    <div class="holder-name">Mira Tolson</div>
    <ul class="contact-list">
      <li><svg><use href="#icon-phone"/></svg>0412 871 964</li>
      <li><svg><use href="#icon-mail"/></svg>altaroutfitters@mailbox-example.com</li>
      <li><svg><use href="#icon-globe"/></svg>www.altaroutfitters.com.au</li>
      <li><svg><use href="#icon-square"/></svg>www.socialpage-example.com/AltarOutfitters</li>
    </ul>
  </section>

  <!-- Option 1, back -->
  <section class="card card-one-back">
    <div class="flourish" role="img" aria-label="Pale mint swirl ornament" style="left:20px;top:-20px;width:200px;height:200px"></div>
    <div class="flourish" role="img" aria-label="Pale mint swirl ornament" style="left:120px;top:170px;width:180px;height:150px"></div>
    <div class="side-band"></div>
    <div class="ceremony-photo photo-garden" role="img" aria-label="Photo of a garden ceremony with white chairs and aisle runner beside a harbour"></div>
    <div class="ceremony-photo photo-beach" role="img" aria-label="Photo of a beach ceremony with rows of white chairs on sand"></div>
    <div class="brand-name">Altar Outfitters</div>
  </section>

  <!-- Option 2, back -->
  <section class="card card-two-back">
    <div class="top-band"></div>
    <div class="flourish" role="img" aria-label="Light mint swirl ornament" style="left:320px;top:0;width:210px;height:130px"></div>
    <div class="flourish" role="img" aria-label="Faint mint swirl ornament" style="left:0;top:190px;width:150px;height:130px"></div>
    <div class="ceremony-photo photo-garden" role="img" aria-label="Photo of a garden ceremony with white chairs and aisle runner beside a harbour"></div>
    <div class="ceremony-photo photo-beach" role="img" aria-label="Photo of a beach ceremony with rows of white chairs on sand"></div>
  </section>
</body>
</html>
```